Young, dynamic furniture company needs a new business card design

We require a new business card design for our modern furniture company which supplies furniture and appliances to the property and development market.
Oakline Furnishings has become one of the leading furniture & appliance suppliers to the property market withing London. With over 10 years experience, we have increased our business to supply not only private landlords and managing agents, but also property developers, housing associations and local councils.
We offer not only a complete range of furniture which includes beds, wardrobes, dining sets and sofas, but also a high quality, full delivery and assembly service to help you with all our furnishing needs.

Target Market(s)

Private landlords, estate agents, letting agents, property management companies

Industry/Entity Type

Business

Contact Information for Business Card

Name,
Title,
Address,
Mobile,
Telephone,
Fax, Website, email address

Font styles to use
Sans Serif

Colors
3176b5
0555a3
85abd2
cfdeed

Requirements
Must have
• All the above information for each of our staff, along with our logo

```html
<!DOCTYPE html>
<html lang="en">
<head>
<meta charset="utf-8">
<title>Oakline Furnishings — Business Card</title>
<link href="https://fonts.googleapis.com/css2?family=Open+Sans:wght@400;600;700&display=swap" rel="stylesheet">
<style>
  :root {
    --navy: #25337a;
    --navy-dark: #1f2b68;
    --blue: #3176b5;
    --blue-deep: #0555a3;
    --blue-soft: #85abd2;
    --blue-pale: #cfdeed;
    --ink: #2a2a35;
    --muted: #6b6f7a;
    --paper: #ffffff;
    --backdrop: #e9ecf1;
  }
  * { box-sizing: border-box; margin: 0; padding: 0; }
  html, body { width: 1200px; height: 886px; overflow: hidden; }
  body {
    background: var(--backdrop);
    font-family: "Open Sans", sans-serif;
    position: relative;
  }
  .card {
    position: absolute;
    top: 283px;
    width: 560px;
    height: 320px;
    box-shadow: 0 6px 18px rgba(20, 30, 60, 0.18);
    overflow: hidden;
  }

  /* Front of card */
  .card-front { left: 20px; background: var(--navy); }
  .card-front .panel {
    position: absolute;
    top: 14px; left: 58px; right: 0; bottom: 14px;
    background: var(--paper);
    clip-path: polygon(0 0, 100% 0, 100% 100%, 46px 100%, 0 calc(100% - 46px));
  }
  .brand {
    position: absolute;
    left: 20px; top: 92px;
    width: 220px;
    display: flex; flex-direction: column; align-items: flex-start;
  }
  .brand-mark { width: 34px; height: 34px; background: var(--blue); flex: none; }
  .brand .brand-mark { margin-bottom: 12px; }
  .brand-name {
    font-size: 17px; font-weight: 400; color: var(--ink);
    text-transform: uppercase; letter-spacing: 0.4px; line-height: 1.1;
    white-space: nowrap;
  }
  .brand-tagline {
    margin-top: 6px;
    font-size: 8.5px; color: var(--muted); text-transform: uppercase; letter-spacing: 1.1px;
    white-space: nowrap;
  }
  .person { position: absolute; left: 262px; top: 26px; }
  .person-name {
    font-size: 22px; font-weight: 700; color: var(--blue); text-transform: uppercase; line-height: 1;
  }
  .person-role {
    font-size: 11px; font-weight: 600; color: var(--navy); text-transform: uppercase;
    margin-top: 4px; text-align: right;
  }
  .details {
    position: absolute; left: 262px; top: 82px; bottom: 18px; right: 16px;
    border-left: 1.5px solid var(--blue);
    padding-left: 16px;
    color: var(--ink); font-size: 12px; line-height: 1.45;
  }
  .address { margin-bottom: 22px; }
  .contact-list { list-style: none; }
  .contact-list li { display: flex; align-items: center; gap: 8px; white-space: nowrap; }
  .contact-list svg { width: 13px; height: 13px; flex: none; fill: var(--navy); }

  /* Back of card */
  .card-back { left: 620px; background: var(--navy); }
  .back-brand {
    position: absolute; left: 0; right: 0; top: 112px;
    display: flex; justify-content: center; align-items: center; gap: 12px;
  }
  .back-brand .brand-mark { width: 26px; height: 26px; background: var(--blue-soft); }
  .back-brand .brand-name { color: var(--paper); font-size: 26px; }
  .back-tagline {
    position: absolute; left: 0; right: 0; top: 152px; text-align: center;
    font-size: 10px; color: var(--blue-pale); text-transform: uppercase; letter-spacing: 1.4px;
  }
  .back-footer {
    position: absolute; left: 40px; right: 40px; bottom: 30px;
    display: flex; align-items: center; gap: 14px;
    color: var(--paper); font-size: 13px;
  }
  .back-footer .rule { height: 1px; background: var(--blue-pale); }
  .back-footer .rule.short { width: 40px; }
  .back-footer .rule.long { flex: 1; }
</style>
</head>
<body>

<section class="card card-front" aria-label="Business card front">
  <div class="panel">
    <div class="brand">
      <span class="brand-mark"></span>
      <span class="brand-name">Oakline Furnishings</span>
      <p class="brand-tagline">Trade Furniture Solutions</p>
    </div>

    <div class="person">
      <p class="person-name">Your Name</p>
      <p class="person-role">Position</p>
    </div>

    <div class="details">
      <p class="address">PO BOX 1234, Address Line 1,<br>Address Line 2,<br>Address Line 3</p>
      <ul class="contact-list">
        <li>
          <svg viewBox="0 0 16 16" aria-hidden="true"><path d="M3.5 1h2.2l1.2 3.2-1.6 1.1a8 8 0 0 0 5.4 5.4l1.1-1.6 3.2 1.2v2.2c0 .8-.7 1.5-1.5 1.5C6.8 15 1 9.2 1 2.5 1 1.7 1.7 1 2.5 1z"/></svg>
          123-456-7890
        </li>
        <li>
          <svg viewBox="0 0 16 16" aria-hidden="true"><path d="M4 1h6l2 2v3H4zM2 7h12a1 1 0 0 1 1 1v4h-3v3H4v-3H1V8a1 1 0 0 1 1-1zm3 5v2h6v-2z"/></svg>
          123-456-7890
        </li>
        <li>
          <svg viewBox="0 0 16 16" aria-hidden="true"><path d="M1 3h14v10H1zm1.5 1.2V12h11V4.2L8 8.6z M2.8 4 8 7.6 13.2 4z"/></svg>
          youremail@oaklinemail.com
        </li>
        <li>
          <svg viewBox="0 0 16 16" aria-hidden="true"><path d="M8 1a7 7 0 1 0 0 14A7 7 0 0 0 8 1zm0 1.3c.9.8 1.6 2.2 1.9 3.7H6.1C6.4 4.5 7.1 3.1 8 2.3zM2.4 7.3h2.4a11 11 0 0 0 0 1.4H2.4a5.7 5.7 0 0 1 0-1.4zm3.7 0h3.8a10 10 0 0 1 0 1.4H6.1a10 10 0 0 1 0-1.4zm5.1 0h2.4a5.7 5.7 0 0 1 0 1.4h-2.4a11 11 0 0 0 0-1.4zM6.1 10h3.8c-.3 1.5-1 2.9-1.9 3.7-.9-.8-1.6-2.2-1.9-3.7z"/></svg>
          www.website.com
        </li>
      </ul>
    </div>
  </div>
</section>

<section class="card card-back" aria-label="Business card back">
  <div class="back-brand">
    <span class="brand-mark"></span>
    <span class="brand-name">Oakline Furnishings</span>
  </div>
  <p class="back-tagline">Trade Furniture Solutions</p>
  <div class="back-footer">
    <span class="rule short"></span>
    <span class="website">www.website.com</span>
    <span class="rule long"></span>
  </div>
</section>

</body>
</html>
```